Figure for a research paper

I am working on designing a figure for a research paper that illustrates the effect of KORA Pathway assessment on student outcomes over time by impacting teacher bias and teacher perception of student growth. I built the attached figure via powerpoint. It includes the very basic elements but it does not look great and I am not sure that it is clearly depicting what I am hoping to illustrate. I would like for you to build an illustration of this idea that i can include in the paper.

```html
<!DOCTYPE html>
<html lang="en">
<head>
<meta charset="utf-8">
<title>KORA Pathway Assessment and Student Outcomes Over Time</title>
<link href="https://fonts.googleapis.com/css2?family=Source+Sans+3:wght@400&display=swap" rel="stylesheet">
<style>
  :root {
    --axis: #185f80;
    --ink: #1a5a7a;
    --growth: #1ec01e;
    --assessment: #e83535;
    --area: #f4f5f7;
    --paper: #ffffff;
  }
  html, body {
    margin: 0;
    padding: 0;
    width: 1200px;
    height: 1200px;
    overflow: hidden;
    background: var(--paper);
  }
  .figure-sheet {
    display: block;
    width: 1200px;
    height: 1200px;
    font-family: "Source Sans 3", "Myriad Pro", sans-serif;
  }
  .axis-line { stroke: var(--axis); stroke-width: 8; stroke-linecap: round; fill: none; }
  .axis-head { fill: var(--axis); }
  .outcome-area { fill: var(--area); }
  .growth-line { stroke: var(--growth); stroke-width: 2; }
  .growth-dot { fill: var(--growth); }
  .assessment-line { stroke: var(--assessment); stroke-width: 2; }
  .assessment-dot { fill: var(--assessment); }
  .pressure-down { fill: var(--growth); }
  .pressure-up { fill: var(--assessment); }
  .axis-title { fill: var(--ink); font-size: 31px; }
  .time-label { fill: var(--ink); font-size: 31px; text-anchor: middle; }
  .force-label { fill: var(--ink); font-size: 22px; }
  .force-label.centered { text-anchor: middle; }
  .figure-number { fill: var(--ink); font-size: 33px; }
</style>
</head>
<body>
<svg class="figure-sheet" viewBox="0 0 1920 1920" xmlns="http://www.w3.org/2000/svg" role="img" aria-label="Two charts of SEL program effectiveness over time, without and with KORA Framework Assessment">

  <!-- Figure 1: without assessment -->
  <g class="chart chart-baseline">
    <polygon class="outcome-area" points="600,602 1350,492 1350,716 600,716"/>
    <line class="axis-line" x1="597" y1="745" x2="597" y2="215"/>
    <polygon class="axis-head" points="573,223 619,223 596,183"/>
    <line class="axis-line" x1="567" y1="720" x2="1510" y2="720"/>
    <polygon class="axis-head" points="1506,697 1506,741 1545,719"/>

    <line class="growth-line" x1="600" y1="602" x2="1356" y2="487"/>
    <circle class="growth-dot" cx="600" cy="602" r="5.5"/>
    <circle class="growth-dot" cx="1356" cy="487" r="5.5"/>

    <g class="force force-bias">
      <rect class="pressure-down" x="693" y="487" width="186" height="17"/>
      <rect class="pressure-down" x="721" y="500" width="13" height="46"/>
      <polygon class="pressure-down" points="707,545 747,545 727,574"/>
      <rect class="pressure-down" x="833" y="500" width="13" height="31"/>
      <polygon class="pressure-down" points="819,530 859,530 839,558"/>
      <text class="force-label centered" x="786" y="464">Teacher Bias</text>
    </g>

    <g class="force force-perception">
      <rect class="pressure-down" x="1123" y="420" width="243" height="17"/>
      <rect class="pressure-down" x="1166" y="433" width="14" height="46"/>
      <polygon class="pressure-down" points="1153,478 1193,478 1173,507"/>
      <rect class="pressure-down" x="1301" y="433" width="14" height="30"/>
      <polygon class="pressure-down" points="1288,462 1328,462 1308,491"/>
      <text class="force-label" x="1138" y="348">Teacher’s inaccurate</text>
      <text class="force-label" x="1138" y="375">perception of student</text>
      <text class="force-label" x="1138" y="402">growth (or learning)</text>
    </g>

    <text class="axis-title" x="358" y="418">Effectiveness of</text>
    <text class="axis-title" x="358" y="455">SEL Program on</text>
    <text class="axis-title" x="358" y="492">the Student</text>
    <text class="time-label" x="1040" y="761">Time</text>
    <text class="figure-number" x="1440" y="802">FIg. 1</text>
  </g>

  <!-- Figure 2: with assessment -->
  <g class="chart chart-assessed">
    <polygon class="outcome-area" points="600,1593 1480,1485 1480,1708 600,1708"/>
    <line class="axis-line" x1="597" y1="1737" x2="597" y2="1080"/>
    <polygon class="axis-head" points="573,1088 619,1088 596,1049"/>
    <line class="axis-line" x1="567" y1="1712" x2="1510" y2="1712"/>
    <polygon class="axis-head" points="1506,1690 1506,1734 1545,1712"/>

    <line class="growth-line" x1="600" y1="1593" x2="1487" y2="1477"/>
    <line class="assessment-line" x1="600" y1="1593" x2="1481" y2="1246"/>
    <circle class="assessment-dot" cx="1481" cy="1246" r="5.5"/>
    <circle class="growth-dot" cx="600" cy="1593" r="5.5"/>
    <circle class="growth-dot" cx="1487" cy="1477" r="5.5"/>

    <g class="force force-bias">
      <rect class="pressure-down" x="820" y="1363" width="195" height="17"/>
      <rect class="pressure-down" x="850" y="1376" width="14" height="85"/>
      <polygon class="pressure-down" points="837,1460 877,1460 857,1489"/>
      <rect class="pressure-down" x="963" y="1376" width="14" height="39"/>
      <polygon class="pressure-down" points="950,1414 990,1414 970,1443"/>
      <text class="force-label centered" x="917" y="1341">Teacher Bias</text>
    </g>

    <g class="force force-perception">
      <rect class="pressure-down" x="1254" y="1192" width="242" height="17"/>
      <rect class="pressure-down" x="1297" y="1205" width="14" height="81"/>
      <polygon class="pressure-down" points="1284,1285 1324,1285 1304,1313"/>
      <rect class="pressure-down" x="1430" y="1205" width="14" height="30"/>
      <polygon class="pressure-down" points="1417,1234 1457,1234 1437,1262"/>
      <text class="force-label" x="1269" y="1121">Teacher’s inaccurate</text>
      <text class="force-label" x="1269" y="1148">perception of student</text>
      <text class="force-label" x="1269" y="1175">growth (or learning)</text>
    </g>

    <g class="force force-assessment">
      <rect class="pressure-up" x="1289" y="1381" width="186" height="17"/>
      <rect class="pressure-up" x="1328" y="1355" width="14" height="30"/>
      <polygon class="pressure-up" points="1315,1356 1355,1356 1335,1328"/>
      <rect class="pressure-up" x="1440" y="1300" width="14" height="85"/>
      <polygon class="pressure-up" points="1427,1301 1467,1301 1447,1272"/>
      <text class="force-label centered" x="1382" y="1429">KORA Framework</text>
      <text class="force-label centered" x="1382" y="1456">Assessment</text>
    </g>

    <text class="axis-title" x="373" y="1326">Effectiveness of</text>
    <text class="axis-title" x="373" y="1363">SEL Program on</text>
    <text class="axis-title" x="373" y="1400">the Student</text>
    <text class="time-label" x="1054" y="1753">Time</text>
    <text class="figure-number" x="1440" y="1812">FIg. 2</text>
  </g>
</svg>
</body>
</html>
```